updated documents

Hi i have included a new picture for the about us section, i have also included the updated word document, all changes have been highlighted.

Thanks,

Leon

```html
<!DOCTYPE html>
<html lang="en">
<head>
<meta charset="utf-8">
<title>Crestline Property Services – About &amp; Services</title>
<link href="https://fonts.googleapis.com/css2?family=Source+Sans+3:wght@300;400;600&display=swap" rel="stylesheet">
<style>
  :root {
    --slate: #6b6c6e;
    --lime: #a9cc38;
    --ink: #3a3a3a;
    --rule: #bdbdbd;
    --paper: #ffffff;
    --backdrop: #efefef;
    --photo-light: #d9dde0;
    --photo-mid: #a9b0b5;
    --photo-dark: #6f777c;
  }
  * { margin: 0; padding: 0; box-sizing: border-box; }
  html, body { width: 1200px; height: 900px; overflow: hidden; }
  body {
    background: var(--backdrop);
    font-family: "Source Sans 3", "Myriad Pro", Arial, sans-serif;
    color: var(--ink);
    position: relative;
  }
  .spread {
    position: absolute;
    left: 101px; top: 95px;
    width: 992px; height: 701px;
    background: var(--paper);
    overflow: hidden;
  }
  .about-panel {
    position: absolute;
    left: 0; top: 0;
    width: 496px; height: 292px;
    background: var(--slate);
  }
  .about-text {
    position: absolute;
    left: 119px; top: 76px;
    width: 318px;
    color: #fff;
    font-size: 12.2px;
    line-height: 15.1px;
  }
  .about-text p + p { margin-top: 6px; }
  .hero-photo {
    position: absolute;
    left: 496px; top: 0;
    width: 496px; height: 292px;
    background: linear-gradient(135deg, var(--photo-light) 0%, var(--photo-mid) 45%, var(--photo-dark) 75%, var(--photo-mid) 100%);
  }
  .services-title {
    position: absolute;
    left: 119px; top: 307px;
    font-size: 30px;
    font-weight: 300;
    color: var(--lime);
    letter-spacing: 0.4px;
  }
  .service-column {
    position: absolute;
    top: 360px;
    width: 170px;
  }
  .service-item {
    border-bottom: 1px solid var(--rule);
    padding-bottom: 7px;
    margin-bottom: 7px;
  }
  .service-item h3 {
    font-size: 11px;
    font-weight: 400;
    color: var(--lime);
    margin-bottom: 5px;
    line-height: 13px;
  }
  .service-item p {
    font-size: 7.9px;
    line-height: 10.8px;
    color: var(--ink);
    padding-right: 4px;
  }
  .col-1 { left: 119px; }
  .col-2 { left: 299px; }
  .col-3 { left: 615px; }
  .col-4 { left: 794px; }
</style>
</head>
<body>
  <main class="spread">
    <section class="about-panel">
      <div class="about-text">
        <p>Crestline Property Services is an Adelaide based company providing general building and office maintenance and refurbishments. We pride ourselves in delivering cost effective high quality services with minimal disturbance to tenants and their occupants.</p>
        <p>Crestline Property Services provides a wide range of services including all major trades Electrical, Data, Plumbing, carpentry, landscaping, and more. With all trades available we can manage their work as required. We also provide preventive maintenance programs to help reduce future reactive works. Our Team have all undertaken police checks and are white card accredited.</p>
      </div>
    </section>

    <div class="hero-photo" role="img" aria-label="Photo of a plumber lying under a sink, reaching up to repair grey drain pipes"></div>

    <h2 class="services-title">Our Services</h2>

    <div class="service-column col-1">
      <article class="service-item">
        <h3>Building repairs and Maintenance</h3>
        <p>The team at Crestline Property Services have extensive skills and experience in both internal and external building repairs and maintenance. Installation and repairs to floor and ceilings systems, doors/locks, appliance repairs, whiteboards, TV screens, picture hanging, patching and paint, vandal repairs, workstations and joinery, plumbing and electrical.</p>
      </article>
      <article class="service-item">
        <h3>Electrical</h3>
        <p>Crestline Property Services provides a wide range of electrical services ranging from Test and tag, Mains services, Switchboard installations, fault finding, RCD testing, data cabling/patching, electrical upgrades and lighting.</p>
      </article>
      <article class="service-item">
        <h3>Planned preventative maintenance</h3>
        <p>Crestline Property Services Offer planned preventive maintenance specifically tailored to the client's requirements. Planned maintenance schedules can be created to prevent breakdowns and costly reactive maintenance in the future. Maintenance programs can include floor and ceiling repairs, light bulb replacements, Test and tagging, Storm water and gutter cleaning.</p>
      </article>
    </div>

    <div class="service-column col-2">
      <article class="service-item">
        <h3>Painting</h3>
        <p>Crestline Property Services pride ourselves in quality and detail ensuring the very best results while being a cost effective and efficient.</p>
      </article>
      <article class="service-item">
        <h3>Signage</h3>
        <p>Crestline Property Services have an experience signage team that specialize in both internal and external signage, decals, promotional banners, window frosting, company logos and design.</p>
      </article>
      <article class="service-item">
        <h3>Office layout changes</h3>
        <p>If you are looking to make some changes to your office either big or small our team can assist with Workstation reconfiguration, internal demolition, Partition/wall installations and even complete office relocations.</p>
      </article>
      <article class="service-item">
        <h3>Appliance repairs</h3>
        <p>Crestline Property Services can repair and replace all of your office appliance's ranging from dishwashers and microwaves to monitors, TV's and projectors.</p>
      </article>
    </div>

    <div class="service-column col-3">
      <article class="service-item">
        <h3>Cleaning</h3>
        <p>Our team offer both internal and external cleaning services including carpark cleaning, window cleaning, carpet dry cleaning, and general office cleaning.</p>
      </article>
      <article class="service-item">
        <h3>Rubbish removal/recycling</h3>
        <p>Crestline Property Services specialize in office rubbish removal, We have a solution to all your rubbish removal needs; including, electronic waste recycling (PCs, monitors, printers, cables etc.), Basement access skip bins, wheelie bins of various sizes, internal demolition services, workstation/furniture removal, rubbish removal/cleanup services.</p>
      </article>
      <article class="service-item">
        <h3>Plumbing</h3>
        <p>Our Plumbing team are experienced and available 24/7 for all your plumbing requirements. Our plumbing services include, water boiler/chiller unit installs and repairs, blocked drains and toilets, roof work and gas fitting.</p>
      </article>
    </div>

    <div class="service-column col-4">
      <article class="service-item">
        <h3>Grounds keeping</h3>
        <p>Let us help with your grounds keeping, our services include, lawn mowing and garden care, carpark sweeping, tree pruning, line marking, gutter cleaning, landscaping, bird and pest management, fencing installs and repairs.</p>
      </article>
      <article class="service-item">
        <h3>Carpentry</h3>
        <p>Crestline Property Services have a dedicated carpentry team that can assist with all your requirements including Partitioning, cupboard installations and all repairs and modifications.</p>
      </article>
      <article class="service-item">
        <h3>Floor /ceiling</h3>
        <p>We can provide floor and ceiling repairs to all types of systems including, suspended ceiling systems and raised floors, ceiling/floor tile replacement, carpet and vinyl replacements and repairs, ceiling access hatches and air vent installs.</p>
      </article>
    </div>
  </main>
</body>
</html>
```